Volora Laundry and Dry Cleaning Poster

We need a Poster and Window Sticker for our Laundry and Dry cleaning shop (VOLORA LAUNDRY AND DRY CLEANING).
info we like on the design. Logo is included
Company Name: Volora Laundry and Dry Cleaning
Slogan: It Comes Back Clean
Location: Kwentu-Dasor, Accra
Working Hours: Mon-Sat 8am to 5pm
Tel: +233 30 781 6242
email:info@voloralaundry.example
website: www.voloralaundry.example
fb: fb.com/voloralaundry

Target Market(s)

Laundry Shop

Colors
33a6d7
9bcb3b

```html
<!DOCTYPE html>
<html lang="en">
<head>
<meta charset="utf-8">
<title>Volora Laundry and Dry Cleaning Poster</title>
<link href="https://fonts.googleapis.com/css2?family=Montserrat:wght@700&family=Oswald:wght@500&family=Roboto:wght@400;700&display=swap" rel="stylesheet">
<style>
  :root {
    --brand-blue: #1ea4db;
    --brand-green: #9bcb3b;
    --paper: #ffffff;
    --backdrop: #eeeeee;
    --photo-warm: #b9a89a;
    --photo-cool: #9fa7ad;
  }
  html, body {
    margin: 0;
    width: 1200px;
    height: 1200px;
    overflow: hidden;
    background: var(--backdrop);
  }
  .poster {
    position: absolute;
    left: 197px;
    top: 30px;
    width: 806px;
    height: 1140px;
    display: block;
    box-shadow: 0 4px 18px rgba(0,0,0,0.12);
  }
  .brand-name { font-family: "Montserrat", sans-serif; font-weight: 700; fill: var(--brand-blue); }
  .headline { font-family: "Oswald", sans-serif; font-weight: 500; fill: var(--paper); }
  .slogan { font-family: "Roboto", sans-serif; font-weight: 400; fill: var(--paper); letter-spacing: 6px; }
  .hours-label { font-family: "Roboto", sans-serif; font-weight: 700; fill: var(--paper); }
  .hours-value { font-family: "Roboto", sans-serif; font-weight: 400; fill: var(--paper); letter-spacing: 1.5px; }
  .contact-text { font-family: "Roboto", sans-serif; font-weight: 400; fill: var(--brand-green); letter-spacing: 1.6px; }
  .icon-fill { fill: var(--brand-blue); }
  .icon-line { fill: none; stroke: var(--brand-blue); stroke-width: 3; }
</style>
</head>
<body>
<svg class="poster" viewBox="0 0 948 1340" xmlns="http://www.w3.org/2000/svg">
  <rect class="poster-paper" width="948" height="1340" fill="var(--paper)"/>

  <!-- header corner accent -->
  <polygon points="743,0 948,0 948,248" fill="var(--brand-blue)"/>

  <!-- brand name -->
  <g class="brand">
    <circle cx="235" cy="123" r="72" fill="var(--brand-blue)"/>
    <text class="brand-name" x="330" y="160" font-size="104">volora</text>
  </g>

  <!-- title band -->
  <rect class="title-band" x="0" y="251" width="948" height="147" fill="var(--brand-green)"/>
  <text class="headline" x="474" y="347" font-size="60" text-anchor="middle">VOLORA LAUNDRY AND DRY CLEANING</text>

  <!-- photo panels -->
  <polygon role="img" aria-label="Photo of a smiling attendant beside bagged dry-cleaned garments"
           points="0,428 168,428 573,833 573,875 0,875" fill="var(--photo-warm)"/>
  <polygon role="img" aria-label="Photo of a worker pouring detergent in a laundromat with washing machines"
           points="418,431 948,431 948,875 843,875" fill="var(--photo-cool)"/>

  <!-- slogan stripe -->
  <polygon class="slogan-stripe" points="191,400 338,400 808,875 653,875" fill="var(--brand-blue)"/>
  <text class="slogan" x="498" y="640" font-size="36" text-anchor="middle"
        transform="rotate(45 498 640)">IT COMES BACK CLEAN</text>

  <!-- lower corner accent -->
  <polygon points="0,878 30,878 363,1340 0,1340" fill="var(--brand-blue)"/>

  <!-- working hours bar -->
  <polygon class="hours-bar" points="55,895 948,895 948,969 113,969" fill="var(--brand-green)"/>
  <text class="hours-label" x="205" y="941" font-size="26">WORKING HOURS :</text>
  <text class="hours-value" x="521" y="941" font-size="25">MON-SAT 8AM TO 5PM</text>

  <!-- contact list -->
  <g class="contact-list">
    <!-- location -->
    <path class="icon-fill" d="M526,1050 a16,16 0 0 1 16,16 c0,13 -16,28 -16,28 c0,0 -16,-15 -16,-28 a16,16 0 0 1 16,-16 z"/>
    <circle cx="526" cy="1066" r="6" fill="var(--paper)"/>
    <text class="contact-text" x="574" y="1080" font-size="21">Kwentu-Dasor, Accra</text>

    <!-- phone -->
    <path class="icon-fill" d="M514,1108 l8,-3 l6,12 l-6,4 c2,7 7,13 13,16 l5,-5 l11,7 l-3,8 c-17,1 -34,-19 -34,-39 z"/>
    <path class="icon-line" d="M530,1107 a12,12 0 0 1 11,11 M531,1099 a20,20 0 0 1 18,18" stroke-width="2.5"/>
    <text class="contact-text" x="574" y="1131" font-size="21">+233 30 781 6242</text>

    <!-- email -->
    <rect class="icon-line" x="510" y="1164" width="32" height="22" rx="1"/>
    <path class="icon-line" d="M510,1164 l16,13 l16,-13" stroke-width="2.5"/>
    <text class="contact-text" x="574" y="1183" font-size="21">info@voloralaundry.example</text>

    <!-- website -->
    <circle class="icon-line" cx="526" cy="1227" r="16"/>
    <ellipse class="icon-line" cx="526" cy="1227" rx="7" ry="16" stroke-width="2"/>
    <path class="icon-line" d="M510,1227 h32 M513,1219 h26 M513,1235 h26" stroke-width="2"/>
    <text class="contact-text" x="574" y="1235" font-size="21">www.voloralaundry.example</text>

    <!-- social -->
    <circle class="icon-fill" cx="526" cy="1279" r="17"/>
    <text class="contact-text" x="574" y="1287" font-size="21">fb.com/voloralaundry</text>
  </g>
</svg>
</body>
</html>
```